Marketing Business Card Design

I am, launching a marketing business where I will contract to market hospitality. I want something funky and fun to go with the name Maple Kettle

Industry/Entity Type

Marketing

Contact Information for Business Card

Nora Feltham-Quince
Maple Kettle
Mobile: +61 2 407 652390
Email: nora@maplekettle.com.au

Requirements
Must have
• Fun and modern
Should not have
• Not conservative

```html
<!DOCTYPE html>
<html lang="en">
<head>
<meta charset="utf-8">
<title>Maple Kettle Mobile – Business Card</title>
<link href="https://fonts.googleapis.com/css2?family=Bebas+Neue&display=swap" rel="stylesheet">
<style>
  :root {
    --ink: #111111;
    --brand-purple: #b42fd8;
    --peach: #f6c7a8;
    --blush: #f2a7a8;
    --cream: #f4e6cf;
    --slate: #5a5d60;
    --mist: #dcdde6;
    --rose: #e06aa8;
    --magenta: #e0056f;
    --magenta-bright: #f20bb8;
    --silver: #a7b0ae;
    --silver-light: #e8eceb;
    --gold: #b8921f;
    --gold-light: #e3d343;
    --white: #ffffff;
  }
  * { margin: 0; padding: 0; box-sizing: border-box; }
  html, body { width: 1200px; height: 720px; overflow: hidden; background: var(--white); }
  .card {
    position: relative;
    width: 1200px;
    height: 720px;
    overflow: hidden;
    font-family: "Bebas Neue", "Arial Narrow", sans-serif;
    color: var(--ink);
  }
  .card__backdrop {
    position: absolute;
    inset: 0;
    background:
      radial-gradient(ellipse 420px 260px at 620px 200px, var(--mist) 0%, rgba(220,221,230,0.85) 55%, rgba(220,221,230,0) 100%),
      radial-gradient(ellipse 500px 140px at 900px 10px, var(--rose) 0%, rgba(224,106,168,0) 100%),
      radial-gradient(ellipse 360px 300px at 120px 360px, var(--cream) 0%, rgba(244,230,207,0) 100%),
      linear-gradient(160deg, var(--blush) 0%, var(--peach) 40%, #c9c4c8 70%, var(--slate) 100%);
  }
  .card__waves {
    position: absolute;
    inset: 0;
    width: 1200px;
    height: 720px;
  }
  .holder-name {
    position: absolute;
    left: 117px;
    top: 118px;
    font-size: 56px;
    line-height: 1;
    letter-spacing: 0.5px;
  }
  .contact {
    position: absolute;
    left: 110px;
    top: 420px;
    font-size: 40px;
    line-height: 46px;
    letter-spacing: 0.3px;
  }
  .brand {
    position: absolute;
    left: 640px;
    top: 128px;
    width: 420px;
    text-align: center;
    color: var(--brand-purple);
    font-size: 84px;
    line-height: 76px;
    letter-spacing: 3px;
  }
</style>
</head>
<body>
  <div class="card">
    <div class="card__backdrop" role="img" aria-label="Abstract backdrop of soft peach, pink and grey geometric shapes"></div>

    <svg class="card__waves" viewBox="0 0 1200 720" aria-hidden="true">
      <defs>
        <linearGradient id="magentaBand" x1="0" y1="0" x2="1" y2="0">
          <stop offset="0" stop-color="var(--magenta)"/>
          <stop offset="0.55" stop-color="var(--magenta-bright)"/>
          <stop offset="1" stop-color="var(--magenta)"/>
        </linearGradient>
        <linearGradient id="silverBand" x1="0" y1="0" x2="1" y2="0">
          <stop offset="0" stop-color="var(--silver)"/>
          <stop offset="0.6" stop-color="var(--silver-light)"/>
          <stop offset="1" stop-color="var(--silver)"/>
        </linearGradient>
        <linearGradient id="goldBand" x1="0" y1="0" x2="1" y2="0">
          <stop offset="0" stop-color="var(--gold)"/>
          <stop offset="0.6" stop-color="var(--gold-light)"/>
          <stop offset="1" stop-color="var(--gold)"/>
        </linearGradient>
      </defs>
      <path class="wave wave--silver" d="M0,520 C350,610 820,610 1200,372 L1200,525 C850,625 350,625 0,530 Z" fill="url(#silverBand)"/>
      <path class="wave wave--gold" d="M480,592 C800,570 1040,480 1200,362 L1200,392 C1040,500 800,585 480,596 Z" fill="url(#goldBand)"/>
      <path class="wave wave--outline" d="M0,518 C350,608 820,608 1200,368" fill="none" stroke="var(--white)" stroke-width="4"/>
      <path class="wave wave--magenta" d="M0,525 C350,622 850,622 1200,518 L1200,720 L0,720 Z" fill="url(#magentaBand)" stroke="var(--white)" stroke-width="4"/>
    </svg>

    <div class="holder-name">Nora Feltham-Quince</div>

    <div class="brand">Maple Kettle<br>Mobile</div>

    <div class="contact">
      <div class="contact__phone">+61 2 407 652390</div>
      <div class="contact__email">NORA@MAPLEKETTLE.COM.AU</div>
    </div>
  </div>
</body>
</html>
```